Création de la plaquette commerciale de la VTR
Besoins
Nous avons besoin d'une plaquette commerciale décrivant l'ensemble des activités de notre entreprise tout en montrant notre dynamisme, notre professionnalisme et disponibilité.
Description de l'entreprise
La V.T.R. est une société de services en ingénierie informatique dont les activités sont :
. INGÉNIERIE : Audit des systèmes d'information, Conseil en informatique et système d'information, Ingénierie informatique (conception, développement, fabrication de système d'information
. INTERNET : Conception et design de site web, hébergement internet
. VAR : Revendeur à valeur ajoutée (matériels, logiciels, périphériques, consommables, ...)
. MAINTENANCE : Maintenance sur site avec contrat
Notre site internet :
www.vtr-lomapo.net
La cible
Notre cible est l'ensemble des professionnels et plus particulièrement les TPE, PME & PMI
Couleurs, favoris et autres exigences:
Notre besoin est :
. une plaquette commerciale au format A3 plié en 2 pour les 4 activités
. des feuillets pour les références ingénierie, web, sociétés

```html
<!DOCTYPE html>
<html lang="fr">
<head>
<meta charset="utf-8">
<title>VTR – Plaquette commerciale</title>
<link href="https://fonts.googleapis.com/css2?family=Oswald:wght@400;600;700&family=Open+Sans:wght@400;600;700&display=swap" rel="stylesheet">
<style>
:root{
  --blue:#1a6fc4;
  --blue-dark:#0b3a78;
  --blue-deep:#062453;
  --blue-light:#d8ecfb;
  --cyan:#3fa9f5;
  --orange:#e8731a;
  --text:#1b2a3a;
  --white:#ffffff;
}
*{box-sizing:border-box;margin:0;padding:0}
html,body{width:1200px;height:2284px;overflow:hidden;background:var(--white)}
body{font-family:"Open Sans",Arial,sans-serif;color:var(--text);font-size:11px;line-height:1.35;position:relative}
h2,h3,.tagline,.cover-name{font-family:"Oswald","Arial Narrow",sans-serif}
.sheet{position:absolute;left:0;width:1200px;overflow:hidden}
.sheet-cover{top:0;height:880px}
.sheet-inner{top:900px;height:860px;background:linear-gradient(180deg,#eef6fd,#fff 40%);font-size:12.5px;line-height:1.4}
.sheet-refs{top:1780px;height:504px;background:var(--blue-deep);display:flex;gap:12px;padding:10px}

.panel{position:absolute;top:0;height:100%;padding:20px 26px}
.panel-left{left:0;width:600px;background:linear-gradient(180deg,#fff,#eaf4fc)}
.panel-cover{left:600px;width:600px;background:radial-gradient(circle at 50% 30%,#3fa9f5 0%,#1a6fc4 35%,#0b3a78 75%,#062453 100%)}

.section-title{font-size:34px;font-weight:700;color:var(--blue-dark);text-transform:uppercase;border-bottom:3px solid var(--blue);line-height:1.1;margin-bottom:8px;letter-spacing:.5px}
.sub-title{font-size:18px;font-weight:600;color:var(--blue);text-transform:uppercase;margin:8px 0 4px}
.mini-title{font-size:10px;font-weight:700;color:var(--blue);text-transform:uppercase;margin:6px 0 2px}
.sheet-inner .mini-title{font-size:11.5px}
.sheet-inner .sub-title{font-size:21px;margin:12px 0 6px}
.sheet-inner p{margin-bottom:8px}
p{margin-bottom:5px}
.link{color:var(--orange);font-weight:600}
ul.dots{list-style:none;margin-bottom:5px}
ul.dots li::before{content:"• ";color:var(--blue)}

.box-tag{display:inline-block;background:var(--blue);color:#fff;font-size:9px;padding:2px 8px;float:right}
.maint-box{background:var(--blue);color:#fff;padding:10px 14px;margin-top:6px;font-size:10px}
.maint-box h4{font-size:10px;text-transform:uppercase;margin-bottom:4px}
.maint-box ul{display:grid;grid-template-columns:1fr 1fr;gap:4px 20px;list-style:none}
.maint-box li::before{content:"› "}
.contact{margin-top:10px;text-align:center;font-size:10px;color:var(--blue-dark)}
.contact strong{display:block;color:var(--blue);font-size:12px;border-top:1px solid var(--blue);padding-top:4px}

.cover-name{position:absolute;left:0;right:0;top:150px;display:flex;align-items:center;justify-content:center;gap:18px;color:var(--white);font-weight:700;font-size:96px;letter-spacing:6px;line-height:1}
.cover-name::before{content:"";width:22px;height:22px;border-radius:50%;background:var(--white)}
.tagline{position:absolute;left:0;right:0;top:560px;text-align:center;color:#fff;font-weight:600;font-size:40px;line-height:1.15}
.tagline b{display:block;font-size:58px;font-weight:700}
.cover-web{position:absolute;right:40px;bottom:40px;color:#fff;font-weight:700;font-size:16px;letter-spacing:1px}

.col{position:absolute;top:0;height:100%;padding:22px 26px}
.col-ing{left:0;width:600px}
.col-soft{left:600px;width:600px}
.audit-diagram{display:block;margin:8px auto}
.two-col{display:grid;grid-template-columns:1fr 1fr;gap:14px;background:var(--blue-light);padding:10px;font-size:11px}
.two-col h4{font-size:11px;color:var(--blue-dark);text-transform:uppercase;margin-bottom:3px}
.soft-box{display:grid;grid-template-columns:1fr 1fr;gap:14px;margin:12px 0}
.promo{background:var(--blue);color:#fff;padding:12px;font-size:11.5px;display:grid;grid-template-columns:1fr 140px;gap:12px}
.promo .shot{height:120px;background:linear-gradient(135deg,#1c1c1c,#b02020)}
.brands{display:grid;grid-template-columns:repeat(5,1fr);gap:22px 10px;margin-top:22px;align-items:center;text-align:center}
.brand{font-family:"Open Sans",sans-serif;font-weight:700;font-size:16px;color:var(--blue-dark)}
.brand::before{content:"";display:inline-block;width:9px;height:9px;background:var(--blue);margin-right:5px;vertical-align:middle}

.ref{flex:1;background:linear-gradient(180deg,#0e4c9a,#062453);border:1px solid #2a7fd0;padding:10px}
.ref h3{font-size:20px;color:#fff;font-weight:400;border-bottom:2px solid var(--cyan);margin-bottom:10px;text-transform:uppercase}
.ref h3 span{text-transform:none}
.logo-grid{display:grid;grid-template-columns:1fr 1fr;gap:18px 10px;background:#fff;padding:16px 10px;height:400px;align-content:start}
.client{font-weight:700;font-size:13px;color:var(--blue-dark);text-align:center}
.client::before{content:"";display:block;width:36px;height:36px;border-radius:50%;background:var(--blue-light);margin:0 auto 4px}
.shot-grid{display:grid;grid-template-columns:1fr 1fr;gap:10px;height:430px}
.shot-grid div{background:linear-gradient(135deg,#8fb8e0,#2d5f96);border:3px solid #fff}
.shot-grid.web div{background:linear-gradient(135deg,#f2f4f7,#5a7ea8)}
.refs-note{color:#bcd;font-size:9px;margin-top:6px}
</style>
</head>
<body>

<section class="sheet sheet-cover">
  <div class="panel panel-left">
    <h2 class="section-title">Internet</h2>
    <h3 class="sub-title">Conception de site web</h3>
    <p>V.T.R. réalise et développe vos projets web sur mesure pour augmenter votre présence sur le web et valoriser votre image de marque avec des créations de haute qualité.</p>
    <p>En tant que spécialiste, nous veillons au respect du délai et de la qualité de votre produit final. Nous sommes compétents dans plusieurs langages de programmation : <span class="link">PHP, HTML, CSS, JAVA</span> et plusieurs technologies web : Pagecraft, Sitebloc, Vitrinex…</p>
    <p><strong>Tous les types de sites Web dynamiques sont réalisables par la V.T.R. :</strong> les blogs, les sites vitrines, les sites e-commerce, les sites d'actualité, les forums et les sites institutionnels.</p>
    <span class="box-tag">Accrédité bureau d'enregistrement du domaine .GA</span>
    <h3 class="sub-title">Hébergement internet</h3>
    <div class="mini-title">Hébergement Linux</div>
    <p>L'hébergement web sous Linux (LAMP : Linux, Apache, MySQL et PHP) est adapté pour les webmasters qui utilisent les fonctions de l'hébergement Linux, comme les langages Perl ou PHP avec des bases MySQL.</p>
    <div class="mini-title">Activités de l'hébergeur web</div>
    <p>La principale activité de l'hébergeur consiste à installer ses serveurs, à les sécuriser, à les protéger contre les pannes et les attaques malveillantes, à les réparer en cas de panne et à installer les technologies souhaitées par les clients.</p>
    <p>L'hébergement internet trouve sa justification pour diverses raisons :</p>
    <ul class="dots">
      <li>la nécessité de sécuriser le service hébergé ;</li>
      <li>la mise à disposition par l'hébergeur de ressources conséquentes ;</li>
      <li>le conseil et les services de support associés.</li>
    </ul>
    <h2 class="section-title">Maintenance</h2>
    <p>Nous mettons en place une maintenance préventive et nous venons régulièrement pour éviter les problèmes graves. Lors de nos visites, nous traitons vos différentes remarques et vous conseillons sur les achats à effectuer.</p>
    <div class="mini-title">La maintenance sur site V.T.R.</div>
    <p>Tout illimité : interventions sur site, télémaintenance, assistance mail et téléphonique et les déplacements sont inclus au contrat de maintenance sur site annuel.</p>
    <div class="maint-box">
      <h4>Nos services inclus au contrat :</h4>
      <ul>
        <li>Un logiciel antivirus par poste</li>
        <li>Intervention au maximum sous une demi-journée</li>
        <li>Un logiciel de télémaintenance par poste</li>
        <li>Frais de déplacement inclus</li>
        <li>Un logiciel de nettoyage et d'optimisation</li>
        <li>Assistance hotline et mail illimitée</li>
        <li>La gestion d'inventaire du parc informatique</li>
        <li>Télémaintenance illimitée</li>
        <li>Un agent de supervision sur chaque poste</li>
        <li>Si la panne est matérielle, diagnostic sur site</li>
        <li>Une visite trimestrielle de contrôle du parc</li>
        <li>Si la panne est logicielle, réparation sur place</li>
        <li>Un audit des performances chaque année</li>
        <li>En cas d'infection, nettoyage complet des postes</li>
      </ul>
    </div>
    <div class="contact">
      <strong>Contact</strong>
      Directeur Général : Marc ONDO | m.ondo@vtr-lomapo.net<br>
      Responsable Commercial : Paul MBADINGA | p.mbadinga@vtr-lomapo.net<br>
      Téléphone : +241 01 23 45 67 | Mobile : +241 07 65 43 21
    </div>
  </div>
  <div class="panel panel-cover">
    <div class="cover-name">VTR</div>
    <div class="tagline">Votre partenaire informatique <b>au Gabon</b></div>
    <div class="cover-web">www.vtr-lomapo.net</div>
  </div>
</section>

<section class="sheet sheet-inner">
  <div class="col col-ing">
    <h2 class="section-title">Ingénierie</h2>
    <p>Le génie informatique ou ingénierie informatique est une discipline qui traite de la conception, du développement et de la fabrication de systèmes informatiques à la fois matériels et logiciels. Les domaines de spécialisation incluent l'architecture de l'ordinateur, la réseautique, la télématique, le génie logiciel et l'intelligence artificielle.</p>
    <h3 class="sub-title">Audit</h3>
    <div class="mini-title">Le service audit de parc informatique</div>
    <p>Un audit informatique a pour objectif principal <span class="link">l'évaluation du niveau de contrôle des risques</span> associés aux activités informatiques ainsi que la bonne adéquation entre le <span class="link">système</span>, l'<span class="link">activité</span> et le <span class="link">fonctionnement</span> de l'entreprise.</p>
    <svg class="audit-diagram" width="520" height="130" viewBox="0 0 520 130" aria-label="Schéma de l'audit">
      <g font-family="Open Sans, sans-serif" font-size="11" fill="#1a6fc4">
        <text x="260" y="70" text-anchor="middle" font-family="Oswald, sans-serif" font-size="26" font-weight="700">AUDIT</text>
        <g stroke="#3fa9f5" stroke-width="1.5" fill="none">
          <line x1="225" y1="60" x2="150" y2="20"/><line x1="225" y1="62" x2="120" y2="50"/>
          <line x1="225" y1="66" x2="110" y2="85"/><line x1="225" y1="70" x2="140" y2="115"/>
          <line x1="295" y1="60" x2="380" y2="30"/><line x1="295" y1="64" x2="390" y2="65"/>
          <line x1="295" y1="70" x2="380" y2="105"/>
        </g>
        <text x="145" y="18" text-anchor="end">CONTRÔLE</text>
        <text x="115" y="52" text-anchor="end">ENJEUX</text>
        <text x="105" y="88" text-anchor="end">CONSEIL</text>
        <text x="135" y="120" text-anchor="end">OUTILS</text>
        <text x="385" y="32">PROCESSUS</text>
        <text x="395" y="68">EXPERTISE</text>
        <text x="385" y="108">JUGEMENT</text>
      </g>
    </svg>
    <div class="two-col">
      <div>
        <h4>Audit d'infrastructure système et réseau</h4>
        <ul class="dots"><li>Analyse des serveurs et des postes clients</li><li>Analyse des services réseaux</li><li>Analyse des applications utilisées</li><li>Analyse du réseau physique et du matériel actif</li></ul>
      </div>
      <div>
        <h4>Audit de sécurité informatique</h4>
        <ul class="dots"><li>Sécurité de l'accès internet et des systèmes</li><li>Sécurité des données et de leurs sauvegardes</li><li>Rapport d'audit et plan d'actions adapté</li></ul>
      </div>
    </div>
    <h3 class="sub-title">Conseil informatique</h3>
    <p>L'informatique est une technologie en perpétuelle évolution. À l'heure de faire un <span class="link">choix</span>, il est difficile pour le non initié de s'y retrouver. Nos prestations de conseil sont là pour vous y aider. À partir de l'étude de vos <span class="link">besoins</span> et de votre <span class="link">budget</span>, nous vous orientons vers la <span class="link">solution</span> la mieux adaptée.</p>
    <div class="mini-title">Missions</div>
    <ul class="dots">
      <li>Estimer les besoins de l'entreprise en termes d'organisation et de ressources</li>
      <li>Suggérer l'amélioration des structures existantes ou leur remplacement</li>
      <li>Accompagner le client tout au long des étapes du projet</li>
    </ul>
  </div>
  <div class="col col-soft">
    <h3 class="sub-title" style="font-size:24px;border-bottom:2px solid var(--blue);margin-top:0">Conception de logiciel</h3>
    <p>La <span class="link">conception de logiciel</span> met en œuvre un ensemble d'activités qui à partir d'une demande d'informatisation d'un processus permettent la conception, l'écriture et la mise au point d'un logiciel jusqu'à sa livraison au demandeur.</p>
    <div class="soft-box">
      <div>
        <div class="mini-title">Développement de logiciel</div>
        <p>Le développement de logiciel consiste à étudier, concevoir, construire, transformer, mettre au point, maintenir et améliorer des logiciels. Ce travail est effectué par une équipe d'ingénieurs conformément à un cahier des charges établi par le client.</p>
      </div>
      <div>
        <p>La répartition des travaux permet d'anticiper le délai et le coût de réalisation. Une partie importante du développement est la mise au point et les tests de non-régression, puis la livraison au client.</p>
      </div>
    </div>
    <div class="promo">
      <p>Codestra 19 est un environnement de développement intégré qui réduit les délais de réalisation et améliore la fiabilité et les performances des applications livrées à nos clients.</p>
      <div class="shot" role="img" aria-label="Visuel de la boîte du logiciel de développement"></div>
    </div>
    <h2 class="section-title" style="margin-top:22px">VAR : revendeur à valeur ajoutée</h2>
    <p>VAR, acronyme de l'anglais Value-Added Reseller, désigne un revendeur (généralement informatique) à valeur ajoutée. Par valeur ajoutée, on entend le fait qu'il exerce un métier de revendeur, mais aussi une activité de service.</p>
    <p>Par exemple, une entreprise peut acheter une unité centrale d'ordinateur à un fournisseur donné, un périphérique d'impression à un autre et un écran d'affichage à un troisième. L'entreprise partenaire ensuite le tout pour en faire un système dédié à la conception assistée par ordinateur.</p>
    <div class="brands">
      <span class="brand">Solmaro</span><span class="brand">Kervan</span><span class="brand">Trelis</span><span class="brand">Netoria</span><span class="brand">Lanvia</span>
      <span class="brand">Comptalis</span><span class="brand">Gestor</span><span class="brand">Orvane</span><span class="brand">Connexo</span><span class="brand">Securis</span>
    </div>
  </div>
</section>

<section class="sheet sheet-refs">
  <div class="ref">
    <h3>Références <span>sociétés</span></h3>
    <div class="logo-grid">
      <span class="client">Relais Santé Komo</span><span class="client">Port Mayumba</span>
      <span class="client">Énergie Okoumé</span><span class="client">Garde Nyanga</span>
      <span class="client">Bâtir Estuaire</span><span class="client">Dossiers Ogooué</span>
      <span class="client">Entreprise Lambaréné</span><span class="client">Caisse Mutuelle Ivindo</span>
    </div>
    <p class="refs-note">Et aussi : Hôtel Nkembo, Pharmacie Akanda, Groupe Tchibanga.</p>
  </div>
  <div class="ref">
    <h3>Références <span>ingénierie</span></h3>
    <div class="shot-grid">
      <div role="img" aria-label="Capture d'un logiciel de gestion réalisé"></div>
      <div role="img" aria-label="Capture d'une application réalisée"></div>
      <div role="img" aria-label="Capture d'un logiciel de gestion des assurés"></div>
      <div role="img" aria-label="Capture d'une application de suivi"></div>
      <div role="img" aria-label="Capture d'un logiciel de pharmacie"></div>
      <div role="img" aria-label="Capture d'un logiciel de facturation"></div>
    </div>
  </div>
  <div class="ref">
    <h3>Références <span>site web</span></h3>
    <div class="shot-grid web">
      <div role="img" aria-label="Capture d'un site de photographie"></div>
      <div role="img" aria-label="Capture d'un site vitrine"></div>
      <div role="img" aria-label="Capture d'un site institutionnel"></div>
      <div role="img" aria-label="Capture d'un site d'entreprise"></div>
      <div role="img" aria-label="Capture d'un site d'hôtel"></div>
      <div role="img" aria-label="Capture d'un site associatif"></div>
    </div>
  </div>
</section>

</body>
</html>
```